Rancher Quill Pet Packaging and Tag Design

Create a design for a label card to attach and hang leather pet toys on in merchandise displays. Card will be of a heavy cardboard stock. The design should be simple with a maximum of 4 colors. We would like for it to be whimsical or cartoonish in nature. The focus of the product line will be directed to Farm and Ranch locations that carry Pet supplies. The leather toys will range from leather shaped farm animals to wildlife animals. They could include chewables such as bones or rope type toys. We are a canadian company who are proud of our heritage. The typical card size will be typically 4-6" wide and 8-10" tall. A caricature of Rancher Quill could become the main company logo
Updates
Target Market(s)
Farm and Ranch shoppers for Pet Toys
Industry/Entity Type
Pet and Farm
Look and feel
Each slider illustrates characteristics of the customer's brand and the style your logo design should communicate.

```html
<!DOCTYPE html>
<html lang="en">
<head>
<meta charset="utf-8">
<title>Rancher Quill – Chewables Leather Toys Hang Tag</title>
<link rel="stylesheet" href="https://fonts.googleapis.com/css2?family=Oswald:wght@500;700&display=swap">
<style>
  :root {
    --backdrop: #e6e6e6;
    --leather-red: #c4432b;
    --leather-red-deep: #9e2f1d;
    --stitch: #f0b08f;
    --panel-light: #ecd3a8;
    --panel-mid: #d9b47f;
    --panel-edge: #7a4a2a;
    --ink: #3d1410;
    --badge: #e9dcc6;
    --art-light: #c99c68;
    --art-dark: #5a3420;
  }
  html, body {
    margin: 0;
    padding: 0;
    overflow: hidden;
    background: var(--backdrop);
  }
  .canvas {
    position: relative;
    width: 1200px;
    height: 1070px;
    overflow: hidden;
    background: var(--backdrop);
    font-family: "Oswald", sans-serif;
    color: var(--ink);
  }
  .tag-shape {
    position: absolute;
    inset: 0;
  }
  .brand-mark {
    position: absolute;
    left: 540px;
    top: 135px;
    width: 120px;
    height: 120px;
    border-radius: 50%;
    background: var(--ink);
  }
  .origin-badge {
    position: absolute;
    left: 712px;
    top: 140px;
    width: 92px;
    height: 92px;
    border-radius: 50%;
    background: var(--badge);
    opacity: 0.85;
  }
  .brand-name {
    position: absolute;
    left: 350px;
    width: 500px;
    top: 268px;
    margin: 0;
    text-align: center;
    font-weight: 700;
    font-size: 56px;
    line-height: 1;
    letter-spacing: 1px;
    color: var(--ink);
  }
  .product-line {
    position: absolute;
    left: 350px;
    width: 500px;
    top: 362px;
    margin: 0;
    text-align: center;
    line-height: 1;
  }
  .product-line .sub {
    display: block;
    font-weight: 500;
    font-size: 30px;
    letter-spacing: 4px;
  }
  .product-line .main {
    display: block;
    margin-top: 4px;
    font-weight: 700;
    font-size: 58px;
    letter-spacing: 1px;
  }
  .dog-portrait {
    position: absolute;
    left: 395px;
    top: 480px;
    width: 410px;
    height: 400px;
    border-radius: 46% 46% 30% 30%;
    background: radial-gradient(ellipse at 50% 45%, var(--art-light) 0%, #9c6b43 55%, var(--art-dark) 100%);
    opacity: 0.75;
  }
  .features {
    position: absolute;
    left: 370px;
    width: 460px;
    top: 905px;
    margin: 0;
    padding: 0;
    list-style: none;
    display: flex;
    justify-content: space-between;
    font-weight: 500;
    font-size: 28px;
    line-height: 1;
  }
</style>
</head>
<body>
<div class="canvas">
  <svg class="tag-shape" width="1200" height="1070" viewBox="0 0 1200 1070" aria-hidden="true">
    <defs>
      <linearGradient id="panelFill" x1="0" y1="0" x2="1" y2="1">
        <stop offset="0" stop-color="var(--panel-light)"/>
        <stop offset="1" stop-color="var(--panel-mid)"/>
      </linearGradient>
    </defs>
    <!-- leather border -->
    <path class="tag-border"
      d="M340,210 Q320,210 320,230 V980 Q320,1000 340,1000 H860 Q880,1000 880,980 V230 Q880,210 860,210 H842 C822,120 722,68 600,68 C478,68 378,120 358,210 Z"
      fill="var(--leather-red)" stroke="var(--leather-red-deep)" stroke-width="3"/>
    <!-- stitching -->
    <path class="tag-stitch"
      d="M344,222 Q332,222 332,234 V976 Q332,988 344,988 H856 Q868,988 868,976 V234 Q868,222 856,222 H832 C812,136 716,80 600,80 C484,80 388,136 368,222 Z"
      fill="none" stroke="var(--stitch)" stroke-width="2" stroke-dasharray="7 5"/>
    <!-- inner panel -->
    <path class="tag-panel"
      d="M350,242 V970 H850 V242 H816 C796,160 706,104 600,104 C494,104 404,160 384,242 Z"
      fill="url(#panelFill)" stroke="var(--panel-edge)" stroke-width="4"/>
    <path class="tag-panel-rule"
      d="M360,250 V960 H840 V250 H808 C788,172 702,114 600,114 C498,114 412,172 392,250 Z"
      fill="none" stroke="var(--panel-edge)" stroke-width="1.5" opacity="0.6"/>
  </svg>

  <div class="origin-badge" role="img" aria-label="Country of origin stamp"></div>
  <div class="brand-mark" role="img" aria-label="Rancher Quill brand mark"></div>
  <h1 class="brand-name">RANCHER QUILL</h1>

  <h2 class="product-line">
    <span class="sub">CHEWABLES</span>
    <span class="main">LEATHERTOYS</span>
  </h2>

  <div class="dog-portrait" role="img" aria-label="Hand-sketched portrait of a happy dog with tongue out"></div>

  <ul class="features">
    <li>DURABLE</li>
    <li>FLEVORED</li>
    <li>TEXTURED</li>
  </ul>
</div>
</body>
</html>
```